TorvaLink.com

We need a new web design for our seo services website at torvalink.com.

Right now we have our homepage, and 2 other pages which we use a html code generator. We need a header and footer and a nice professional looking design to showcase our seo plans.

As for the logo we'll use our company torvagrid.com logo Torva and change Grid to Link and Systems to Search Engine Marketing.

We also like to display our brivopages widget and author alert sign up box.

```html
<!DOCTYPE html>
<html lang="en">
<head>
<meta charset="utf-8">
<title>TorvaLink – SEO Services</title>
<link href="https://fonts.googleapis.com/css2?family=Montserrat:wght@400;600;700&family=Open+Sans:wght@400;600;700&display=swap" rel="stylesheet">
<style>
:root{
  --teal:#1bbdb1;
  --teal-dark:#0aa89c;
  --teal-mid:#18bdb0;
  --teal-light:#25cbbf;
  --ink:#2f3a40;
  --grey:#8a9196;
  --line:#e3e6e7;
  --red:#e0324b;
  --brand:#1d3f8f;
  --footer:#2d3134;
  --footer-bar:#232628;
  --footer-text:#7d8488;
  --footer-head:#5d6468;
}
*{box-sizing:border-box;margin:0;padding:0}
html,body{width:960px;height:1200px;overflow:hidden;background:#fff}
body{font-family:"Open Sans",Verdana,sans-serif;color:var(--ink)}
.stage{position:absolute;left:4px;top:0;width:1190px;height:1500px;transform:scale(.8);transform-origin:0 0}
.abs{position:absolute}
.head-font{font-family:"Montserrat",Verdana,sans-serif}

/* header */
.brand{left:243px;top:40px;font-family:"Montserrat",sans-serif;font-weight:700;color:var(--brand);font-size:19px;letter-spacing:-.5px;line-height:1}
.brand small{display:block;font-size:7px;letter-spacing:0;text-align:right;margin-top:2px}
.nav{left:520px;top:31px;display:flex;font-size:8px;color:var(--grey)}
.nav a{display:block;padding:13px 15px 0;color:inherit;text-decoration:none}
.nav a.active{color:var(--teal);border-top:2px solid var(--teal);padding-top:11px}

/* hero */
.hero{left:218px;top:73px;width:732px;height:197px;background:radial-gradient(ellipse at 45% 45%,#b5bbbf 0%,#949ca1 45%,#6f787e 100%)}
.hero-art{left:47px;top:30px;width:283px;height:112px;background:linear-gradient(#dfe2e4,#9aa0a4);border-radius:3px}
.hero h2{left:388px;top:33px;font-size:18px;color:#fff;letter-spacing:1.5px;font-weight:700}
.hero h3{left:388px;top:57px;font-size:13px;color:var(--ink);font-weight:700;letter-spacing:.6px}
.spec{font-size:8px;color:#3d474d;letter-spacing:.4px}
.spec b{font-weight:700}
.price-box{left:387px;top:125px;width:321px;height:31px;background:rgba(80,88,94,.45);border:1px solid rgba(255,255,255,.15);border-radius:2px}
.price-box .from{left:16px;top:9px;font-size:5.5px;color:#e7eaeb;line-height:6px;text-align:center}
.price-box .amt{left:66px;top:4px;font-size:17px;color:#fff;font-weight:700}
.price-box .btn{left:195px;top:5px;width:118px;height:16px;background:var(--teal);color:#fff;font-size:7px;text-align:center;line-height:16px;border-radius:1px}
.dots{left:564px;top:261px;display:flex;gap:6px}
.dots i{width:8px;height:8px;border-radius:50%;background:#3a4145}
.dots i:first-child{background:var(--teal)}

/* intro boxes */
.intro{left:243px;top:300px;width:683px;height:238px;display:flex}
.intro-box{flex:1;color:#fff;text-align:center;padding:24px 20px 0}
.intro-box:nth-child(1){background:var(--teal-dark)}
.intro-box:nth-child(2){background:var(--teal-mid)}
.intro-box:nth-child(3){background:var(--teal-light)}
.intro-icon{width:66px;height:45px;margin:0 auto;border-radius:50%;background:rgba(255,255,255,.18);display:flex;align-items:center;justify-content:center}
.intro-box h4{font-family:"Montserrat",sans-serif;font-size:13px;font-weight:700;letter-spacing:.8px;margin:20px 0 4px}
.intro-box p{font-family:"Montserrat",sans-serif;font-size:8.4px;line-height:11.2px;letter-spacing:.15px}

/* plans */
.plans{left:218px;top:568px;width:732px;height:294px;background:#f7f8f8}
.section-title{width:100%;text-align:center;font-family:"Montserrat",sans-serif;font-size:22px;font-weight:700;letter-spacing:1.2px;color:var(--ink)}
.section-title em{font-style:normal;color:var(--teal)}
.section-sub{width:100%;text-align:center;font-size:8px;color:#a3a9ad}
.plan{top:98px;width:160px;height:160px;background:#fff;box-shadow:0 1px 2px rgba(0,0,0,.08)}
.plan-name{height:22px;background:var(--teal);color:#fff;font-size:8.5px;text-align:center;line-height:24px;letter-spacing:.4px}
.plan-price{height:65px;background:linear-gradient(#fff,#e4e6e6);text-align:center;padding-top:14px;font-family:"Montserrat",sans-serif;font-weight:700;font-size:19px;color:#3a4246}
.plan-price span{display:block;font-size:7.5px;font-family:"Open Sans",sans-serif;color:#555;margin-top:4px}
.plan-feature{height:45px;padding:14px 0 0 40px;font-size:9px;line-height:11px;color:#444;position:relative;letter-spacing:.3px}
.plan-feature svg{position:absolute;left:22px;top:15px}
.plan-btn{height:28px;background:var(--teal);color:#e8fffd;font-size:8.5px;text-align:center;line-height:28px;letter-spacing:.4px}

/* features */
.feature{background:#fff;border:1px solid var(--line);box-shadow:0 1px 2px rgba(0,0,0,.06)}
.feature h5{position:absolute;left:15px;top:6px;font-size:9.5px;font-weight:600;letter-spacing:.6px;color:#333;line-height:10.5px}
.feature .rule{position:absolute;left:0;top:26px;width:165px;height:1px;background:var(--line)}
.feature p{position:absolute;left:15px;top:37px;width:120px;font-size:7px;line-height:11.1px;color:#9a9fa3;letter-spacing:.2px}
.feature .more{position:absolute;left:17px;width:57px;height:14px;border:1px solid #e9ebec;font-size:7px;font-weight:700;color:#7b8185;text-align:center;line-height:12px;background:#fafafa}
.feature .art{position:absolute;background:linear-gradient(135deg,#e9eef1,#aab4bb);border-radius:2px}
.badge{position:absolute;width:36px;height:36px;border-radius:50%;background:#fff;border:1px solid #dfe2e3;text-align:center;font-size:5.5px;line-height:6px;color:#555;padding-top:5px}
.badge b{display:block;color:var(--red);font-size:9px;line-height:9px;font-style:italic;font-weight:600}

/* footer */
.footer{left:218px;top:1312px;width:732px;height:185px;background:var(--footer)}
.footer h6{position:absolute;top:24px;font-size:8px;font-weight:600;color:var(--footer-head);letter-spacing:.7px;line-height:10px}
.footer ul{position:absolute;top:42px;list-style:none;font-size:7.3px;color:var(--footer-text);line-height:15.2px;letter-spacing:.2px}
.footer ul li::before{content:"";display:inline-block;width:2px;height:2px;background:var(--teal);margin:0 7px 2px 0;vertical-align:middle}
.alert-form{position:absolute;left:25px;top:50px;display:flex;width:150px;height:13px}
.alert-form span{flex:1;background:#3a3f42;border:1px solid #454b4e;font-size:6.5px;color:#737a7e;line-height:11px;padding-left:5px}
.alert-form b{width:46px;background:var(--teal);color:#fff;font-size:6.5px;font-weight:600;text-align:center;line-height:13px}
.contact{position:absolute;left:25px;font-size:7.5px;color:#9aa3a6;display:flex;align-items:center;gap:10px}
.contact a{color:#9aa3a6}
.footer-bar{left:218px;top:1477px;width:732px;height:23px;background:var(--footer-bar)}
.footer-bar .copy{left:25px;top:6px;font-size:6.5px;color:#4f5558}
.socials{left:370px;top:7px;display:flex;gap:15px}
.socials i{width:8px;height:8px;border-radius:50%;background:#1a8f88}
</style>
</head>
<body>
<div class="stage">

  <!-- header -->
  <div class="abs brand">TorvaLink<small>Search Engine Marketing</small></div>
  <nav class="abs nav">
    <a class="active">Home</a><a>Services</a><a>Link Building</a><a>Web-Design</a><a>Blog</a><a>Contact us</a>
  </nav>

  <!-- hero -->
  <section class="abs hero">
    <div class="abs hero-art" role="img" aria-label="Stack of three rack-mounted servers"></div>
    <h2 class="abs head-font">EXTREME PLAN</h2>
    <h3 class="abs head-font">Powerful HostDeck shared hosting plan.</h3>
    <div class="abs spec" style="left:388px;top:83px">&#9745; <b>96 MB</b> Memory</div>
    <div class="abs spec" style="left:537px;top:83px">&#9745; <b>20</b> Addon Domains</div>
    <div class="abs spec" style="left:388px;top:101px">&#9745; <b>10 GB</b> Storage</div>
    <div class="abs spec" style="left:537px;top:101px">&#9745; <b>400 GB</b> Monthly Traffic</div>
    <div class="abs price-box">
      <div class="abs from">YEARLY<br>FROM</div>
      <div class="abs amt head-font">$69</div>
      <div class="abs btn">View all available plans</div>
    </div>
  </section>
  <div class="abs dots"><i></i><i></i><i></i></div>

  <!-- intro -->
  <section class="abs intro">
    <div class="intro-box">
      <div class="intro-icon">
        <svg width="30" height="26" viewBox="0 0 30 26" fill="none" stroke="#fff" stroke-width="1.8" stroke-linejoin="round"><rect x="3" y="11" width="5" height="12"/><path d="M8 12l5-8c2-2 4-1 3 2l-1 4h8c2 0 3 2 2 3l-2 8c-1 2-2 2-3 2H8"/></svg>
      </div>
      <h4>About Us</h4>
      <p>TorvaLink Internet Marketing and Search Engine Optimization Services Technology is a digital marketing agency that offers everything you need to have a successful online presence. Increase traffic to your website. Attract new customers. Improve your search engine rankings. Publish content and videos on social networking sites.</p>
    </div>
    <div class="intro-box">
      <div class="intro-icon">
        <svg width="28" height="26" viewBox="0 0 28 26" fill="#fff"><path d="M26 2c-7 0-12 4-15 9l-5 1-4 4 6 1 3 3 1 6 4-4 1-5c5-3 9-8 9-15z"/></svg>
      </div>
      <h4>Our SEO Tools</h4>
      <p>Search engines focus on rewarding those sites that offer people excellent user experiences and valuable content. Our SEO techniques are not only effective, but also meaningful. We focus on creating websites people like visiting and search engines like seeing.Our SEO services definitely give you long-lasting results.</p>
    </div>
    <div class="intro-box">
      <div class="intro-icon">
        <svg width="32" height="24" viewBox="0 0 32 24" fill="none" stroke="#fff" stroke-width="1.8" stroke-linejoin="round"><path d="M4 10c0-5 5-8 11-8s11 3 11 8-5 8-11 8c-2 0-3 0-4-1l-6 3 2-4c-2-1-3-4-3-6z"/><path d="M26 9c2 1 4 3 4 6 0 2-1 3-2 4l1 4-4-2c-2 1-5 1-7 0"/></svg>
      </div>
      <h4>Customer Support</h4>
      <p>We provide businesses with professional consulting and support services 24/7.We also provide technical support professionals to support customer support and services for your growing product lines round the clock.We work with you to develop a customized and winning telephone support team. Because, Your work is our work.</p>
    </div>
  </section>

  <!-- plans -->
  <section class="abs plans">
    <h2 class="abs section-title" style="top:30px">Our<em>Plans</em> &amp; <em>Pricing</em></h2>
    <div class="abs section-sub" style="top:62px">Our Hosting plans in detail. choose the right plan for you!</div>

    <div class="abs plan" style="left:25px">
      <div class="plan-name">Silver Plan</div>
      <div class="plan-price">$500<span>/month</span></div>
      <div class="plan-feature"><svg width="12" height="9" viewBox="0 0 12 9"><path d="M1 5l3 3 7-7" fill="none" stroke="#5cb531" stroke-width="2"/></svg>Up to 10<br>Keywords</div>
      <div class="plan-btn">Read More</div>
    </div>
    <div class="abs plan" style="left:199px">
      <div class="plan-name">Gold Plan</div>
      <div class="plan-price">$750<span>/month</span></div>
      <div class="plan-feature"><svg width="12" height="9" viewBox="0 0 12 9"><path d="M1 5l3 3 7-7" fill="none" stroke="#5cb531" stroke-width="2"/></svg>Up to 20<br>Keywords</div>
      <div class="plan-btn">Read More</div>
    </div>
    <div class="abs plan" style="left:374px">
      <div class="plan-name">Platinum Plan</div>
      <div class="plan-price">$ 1200<span>/month</span></div>
      <div class="plan-feature"><svg width="12" height="9" viewBox="0 0 12 9"><path d="M1 5l3 3 7-7" fill="none" stroke="#5cb531" stroke-width="2"/></svg>Up to 30<br>Keywords</div>
      <div class="plan-btn">Read More</div>
    </div>
    <div class="abs plan" style="left:548px">
      <div class="plan-name">Platinum Plus Plan</div>
      <div class="plan-price">$ 1300<span>/month</span></div>
      <div class="plan-feature"><svg width="12" height="9" viewBox="0 0 12 9"><path d="M1 5l3 3 7-7" fill="none" stroke="#5cb531" stroke-width="2"/></svg>Up to 40<br>Keywords</div>
      <div class="plan-btn">Read More</div>
    </div>
  </section>

  <!-- key features -->
  <h2 class="abs section-title" style="left:0;top:892px;width:1170px">Key Features of <em>Torva Link</em></h2>
  <div class="abs section-sub" style="left:0;top:923px;width:1170px">Our Hosting plans in detail. choose the right plan for you!</div>

  <article class="abs feature" style="left:243px;top:966px;width:217px;height:142px">
    <h5>WEBSITE AUDIT</h5><span class="rule"></span>
    <p>Insightful audits that help you understand what work needs to be done and what the website can rank for. Our comprehensive site audit maximizes the effects of our methodology.</p>
    <span class="more" style="top:117px">Read more</span>
    <div class="art" style="left:118px;top:90px;width:98px;height:50px" role="img" aria-label="Website audit reports on screens"></div>
  </article>
  <div class="badge" style="left:424px;top:958px">starting<b>$1.99</b>/month</div>

  <article class="abs feature" style="left:476px;top:966px;width:217px;height:142px">
    <h5>WEBSITE OPTIMIZATION</h5><span class="rule"></span>
    <p>We will optimize all key aspects of your targeted pages. Our optimization process ensures your website will be ready to rank once we begin our off-page marketing efforts.</p>
    <span class="more" style="top:117px">Read more</span>
    <div class="art" style="left:134px;top:62px;width:82px;height:78px" role="img" aria-label="Server racks in a data centre"></div>
  </article>
  <div class="badge" style="left:657px;top:958px">starting<b>$1.99</b>/month</div>

  <article class="abs feature" style="left:709px;top:966px;width:217px;height:131px">
    <h5>RICH SERPA LISTINGS</h5><span class="rule"></span>
    <p>We'll advise you on how to get the best listing you can in the search results pages. These types of listings get more clicks because of the dynamic information.</p>
    <span class="more" style="top:105px">Read more</span>
    <div class="art" style="left:128px;top:84px;width:88px;height:46px;background:linear-gradient(135deg,#d7eefb,#3e8fd6)" role="img" aria-label="Blue shopping cart"></div>
  </article>
  <div class="badge" style="left:890px;top:958px">starting<b>$1.99</b>/month</div>

  <article class="abs feature" style="left:243px;top:1122px;width:217px;height:152px">
    <h5>CITATION BUILDING &amp; LINK<br>DEVELOPMENT</h5><span class="rule" style="top:28px"></span>
    <p style="top:43px">We develop &amp; publish content with the user in mind. Your company will be published on high authority websites that help build quality back links, rank and create great PR.</p>
    <span class="more" style="top:128px">Read more</span>
    <div class="art" style="left:130px;top:128px;width:80px;height:22px;background:linear-gradient(135deg,#dbe8f6,#5d8fc8)" role="img" aria-label="Web domain lettering graphic"></div>
  </article>
  <div class="badge" style="left:424px;top:1114px">starting<b>$1.99</b>/month</div>

  <article class="abs feature" style="left:476px;top:1122px;width:217px;height:126px">
    <h5>CONTENT MARKETING</h5><span class="rule"></span>
    <p>We'll start getting the word out about your business quickly. In Month 1 we do things like Press Releases, Magazine Features, and Social Sharing.</p>
    <span class="more" style="top:106px">Read more</span>
    <div class="art" style="left:132px;top:80px;width:84px;height:44px;background:linear-gradient(135deg,#dfe4e8,#3d4a55)" role="img" aria-label="Desktop, laptop and phone showing content"></div>
  </article>
  <div class="badge" style="left:657px;top:1114px">starting<b>$1.99</b>/month</div>

  <article class="abs feature" style="left:709px;top:1110px;width:217px;height:142px">
    <h5>REPORTING AND STRATEGY</h5><span class="rule"></span>
    <p>Our live dashboard always has up to date traffic information and search results rankings. You can log in at any time, or get a comprehensive PDF report showing rankings and traffic.</p>
    <span class="more" style="top:118px">Read more</span>
    <div class="art" style="left:146px;top:98px;width:70px;height:42px;background:linear-gradient(135deg,#eef2f6,#8fb2d6)" role="img" aria-label="Analytics report documents"></div>
  </article>
  <div class="badge" style="left:890px;top:1102px">starting<b>$1.99</b>/month</div>

  <!-- footer -->
  <footer class="abs footer">
    <h6 style="left:25px">Dalen Arvo's Expert Author<br>Email Alerts</h6>
    <div class="alert-form"><span>Your email</span><b>Sign up</b></div>
    <div class="contact" style="top:70px">
      <svg width="11" height="9" viewBox="0 0 11 9" fill="#1fb5a9"><path d="M5.5 0L0 4.5h1.5V9h3V6h2v3h3V4.5H11z"/></svg>Ravenport, INDIA
    </div>
    <div class="contact" style="top:86px">
      <svg width="11" height="10" viewBox="0 0 11 10" fill="#1fb5a9"><path d="M2 0l2 2.5-1 1.5c1 1.5 2 2.5 3.5 3.5l1.5-1 2.5 2-1.5 1.5C5 9.5 1 5 .5 1.5z"/></svg>+1 555 010 2299
    </div>
    <div class="contact" style="top:102px">
      <svg width="11" height="8" viewBox="0 0 11 8" fill="none" stroke="#1fb5a9" stroke-width="1.3"><rect x=".7" y=".7" width="9.6" height="6.6"/><path d="M.7 .7l4.8 3.8 4.8-3.8"/></svg><a>hello@torvalink.com</a>
    </div>

    <h6 style="left:200px">Navigation</h6>
    <ul style="left:200px"><li>Web Hosting</li><li>Web Designing</li><li>Features</li><li>Social Media Marketing</li><li>Dedicated Servers</li><li>Domain Registration</li></ul>

    <h6 style="left:316px">Useful Links</h6>
    <ul style="left:316px;width:100px;line-height:13px;top:43px"><li>Proin gravida nibh vel velit auctor aliquet venen</li><li style="margin-top:2px">Aenean sollicitudin</li><li style="margin-top:2px">Lorem quis bibendum</li><li style="margin-top:2px">Lorem ipsum Dolor</li><li style="margin-top:2px">Dolor sit Amet</li></ul>

    <h6 style="left:432px">Recent Posts</h6>
    <ul style="left:432px"><li>Home</li><li>About</li><li>Features</li><li>Blog</li><li>Works</li><li>Contacts</li></ul>

    <h6 style="left:548px">Articles by Dalen Arvo</h6>
  </footer>
  <div class="abs footer-bar">
    <div class="abs copy">© 2012 Privacy Policy</div>
    <div class="abs socials"><i></i><i></i><i></i><i></i><i></i><i></i><i></i><i></i><i></i><i></i><i></i><i></i></div>
  </div>

</div>
</body>
</html>
```